Business Card for Consulting Company

I would need a business card for my consulting company - the company brand and logos are defined and shared as part of this project. The proposed design for the business card can be reused as inspiration for my email signature.

```html
<!DOCTYPE html>
<html lang="en">
<head>
<meta charset="utf-8">
<title>Lumenway — Business Card</title>
<link rel="stylesheet" href="https://fonts.googleapis.com/css2?family=Source+Sans+3:wght@400;700&display=swap">
<style>
  :root {
    --backdrop: #e8f4fa;
    --charcoal: #444444;
    --teal: #1aacaa;
    --white: #ffffff;
    --ink: #222222;
  }
  * { margin: 0; padding: 0; box-sizing: border-box; }
  html, body {
    width: 1066px;
    height: 1200px;
    overflow: hidden;
    background: var(--backdrop);
    font-family: "Source Sans 3", sans-serif;
  }
  .canvas { position: relative; width: 1066px; height: 1200px; }

  .card {
    position: absolute;
    left: 106px;
    width: 854px;
    height: 488px;
    overflow: hidden;
  }
  .card--front { top: 72px; background: var(--charcoal); }
  .card--back  { top: 640px; background: var(--white); }

  .corner-shape { position: absolute; display: block; }
  .card--front .corner-shape { right: 0; bottom: 0; }
  .card--back .corner-shape  { left: 0; top: 0; }

  .brand {
    position: absolute;
    display: flex;
    align-items: center;
    gap: 14px;
    font-weight: 700;
    color: var(--white);
  }
  .brand__dot { border-radius: 50%; background: var(--teal); flex: none; }

  .card--front .brand {
    left: 0; right: 0; top: 200px;
    justify-content: center;
    font-size: 66px;
    letter-spacing: 1px;
  }
  .card--front .brand__dot { width: 30px; height: 30px; }

  .card--back .brand {
    left: 28px; top: 392px;
    font-size: 34px;
    gap: 10px;
    color: var(--charcoal);
  }
  .card--back .brand__dot { width: 18px; height: 18px; }

  .identity {
    position: absolute;
    right: 23px;
    top: 68px;
    width: 243px;
  }
  .identity__name {
    font-size: 40px;
    font-weight: 700;
    line-height: 1;
    color: var(--charcoal);
    white-space: nowrap;
  }
  .identity__first { color: var(--teal); }
  .identity__role {
    font-size: 26px;
    font-weight: 400;
    color: var(--charcoal);
    line-height: 1.2;
    margin-top: 4px;
    letter-spacing: 0.3px;
  }
  .identity__rule {
    height: 2px;
    background: var(--teal);
    margin-top: 14px;
    margin-left: 2px;
  }

  .contact {
    position: absolute;
    right: 23px;
    top: 348px;
    text-align: right;
    font-style: normal;
    font-size: 25px;
    line-height: 34.5px;
    color: var(--ink);
    letter-spacing: 0.4px;
  }
</style>
</head>
<body>
<main class="canvas">

  <section class="card card--front" aria-label="Card front">
    <svg class="corner-shape" width="218" height="218" viewBox="0 0 218 218" aria-hidden="true">
      <path d="M218 0 A218 218 0 0 0 0 218 L218 218 Z" fill="var(--teal)"/>
    </svg>
    <div class="brand">
      <span class="brand__dot"></span>
      <span class="brand__name">Lumenway</span>
    </div>
  </section>

  <section class="card card--back" aria-label="Card back">
    <svg class="corner-shape" width="212" height="212" viewBox="0 0 212 212" aria-hidden="true">
      <path d="M0 0 L212 0 A212 212 0 0 1 0 212 Z" fill="var(--charcoal)"/>
    </svg>

    <div class="identity">
      <h1 class="identity__name"><span class="identity__first">Julien</span> Morel</h1>
      <p class="identity__role">Founder &amp; CEO</p>
      <div class="identity__rule"></div>
    </div>

    <address class="contact">
      <div class="contact__phone">+41 78 412 36 80</div>
      <div class="contact__email">julien.m@lumenway.ch</div>
      <div class="contact__web">www.lumenway.ch</div>
    </address>

    <div class="brand">
      <span class="brand__dot"></span>
      <span class="brand__name">Lumenway</span>
    </div>
  </section>

</main>
</body>
</html>
```